Design a Flyer/Poster for a Mountain Adventure Event

We need a flyer designed to be printed on 8.5" x 11" paper to advertise an event entitled Ridgeline Quest 2014. The copy has already been written. The end result will need to be delivered in a fully editable format (Adobe Illustrator or other Adobe product is preferred). All components of the final deliverable file must be easily editable with appropriate software, as details of this event may change before printing. The final deliverable must also be in a high resolution (min 300dpi) for glossy printing at 8.5" x 11" printed size.

This event is still in concept phase, and the website does not yet exist. Ideas for images are attached below - I do not have rights to use those particular images. In addition to the photo ideas, I have attached versions of the logo for the organization that will benefit from the event (Institute for Glacier & Frost Research). One of those logos will need to be used (probably towards bottom of flyer/poster) with the text: Benefiting the Institute for Glacier & Frost Research

Text for Flyer/Poster:
Ridgeline Quest 2014
June 15 - 30

1. Run/Hike in the Mountains between June 15-30, 2014
2. Track it with GPS or Satellite
3. Follow your Competitors online

Compete for:
Most Elevation Gain
Most Miles
Most Summits
Best Photos
Best Family Adventures

Prizes awarded by Age Class, Gender, Individuals & Teams
You could win $1,000!

Where:
Mountains of your Choice

Registration: $99 (Limited to 500 Participants)
Optional: Rent a Trekbeam X4TM with Unlimited Tracking: $99

Benefiting the Institute for Glacier & Frost Research

```html
<!DOCTYPE html>
<html lang="en">
<head>
<meta charset="utf-8">
<title>Ridgeline Quest 2014 – Flyer</title>
<link rel="stylesheet" href="https://fonts.googleapis.com/css2?family=Bree+Serif&display=swap">
<style>
  :root {
    --sky-top: #0c4fa8;
    --sky-mid: #2b7fd6;
    --sky-glow: #9fd3f5;
    --ridge-dark: #0a0d14;
    --banner: #ffffff;
    --accent: #f6b13c;
    --accent-text: #f3a92e;
    --text-light: #ffffff;
  }
  * { box-sizing: border-box; margin: 0; padding: 0; }
  html, body { width: 927px; height: 1200px; overflow: hidden; background: #000; }
  .flyer {
    position: relative;
    width: 927px;
    height: 1200px;
    overflow: hidden;
    font-family: "Bree Serif", Georgia, serif;
    color: var(--text-light);
  }
  .hero-photo {
    position: absolute; inset: 0;
    background:
      radial-gradient(circle at 79% 50%, rgba(255,255,255,0.95) 0, var(--sky-glow) 6%, rgba(80,160,230,0.3) 24%, transparent 42%),
      linear-gradient(180deg, var(--sky-top) 0%, var(--sky-mid) 38%, #123a6a 62%, var(--ridge-dark) 78%, #050608 100%);
  }
  .banner {
    position: absolute;
    background: var(--banner);
    color: var(--accent-text);
    display: flex; align-items: center; justify-content: center;
    box-shadow: 0 2px 6px rgba(0,0,0,0.25);
  }
  .banner--title {
    left: 88px; top: 84px; width: 762px; height: 98px;
    transform: rotate(-3.2deg);
    font-size: 54px;
  }
  .banner--dates {
    left: 77px; top: 282px; width: 392px; height: 86px;
    transform: rotate(2deg);
    font-size: 52px;
  }
  .banner--url {
    left: 530px; top: 633px; width: 397px; height: 48px;
    font-size: 23px; justify-content: flex-start; padding-left: 22px;
  }
  .step-badge {
    position: absolute;
    width: 56px; height: 56px; border-radius: 50%;
    background: var(--accent);
    color: var(--text-light);
    font-size: 24px;
    display: flex; align-items: center; justify-content: center;
  }
  .steps { position: absolute; left: 151px; top: 433px; list-style: none; }
  .steps li { font-size: 20.5px; line-height: 38px; }
  .details { position: absolute; left: 151px; top: 602px; font-size: 18.5px; line-height: 25.5px; }
  .details .indent { padding-left: 35px; }
  .details .group { margin-bottom: 8px; }
  .details .line { margin-bottom: 12px; }
  .sponsor {
    position: absolute; left: 70px; top: 1098px;
    display: flex; align-items: center; gap: 12px;
    font-size: 17px;
  }
  .sponsor__mark { width: 46px; height: 46px; border-radius: 50%; background: #4a9ed8; flex: none; }
  .sponsor__name { width: 190px; line-height: 17px; font-size: 13.5px; }
  .sponsor__note { font-size: 17px; }
</style>
</head>
<body>
<main class="flyer">
  <div class="hero-photo" role="img" aria-label="Photo of a hiker silhouetted on a mountain summit, arm raised, against a bright blue sky with a sunburst"></div>

  <h1 class="banner banner--title">Ridgeline Quest 2014</h1>
  <h2 class="banner banner--dates">June 15–30</h2>

  <span class="step-badge" style="left:70px;top:417px">1.</span>
  <span class="step-badge" style="left:44px;top:456px">2.</span>
  <span class="step-badge" style="left:70px;top:493px">3.</span>
  <span class="step-badge" style="left:44px;top:532px">4.</span>
  <ol class="steps">
    <li>Run/Hike in the Mountains between June 15–30, 2014</li>
    <li>Track it with GPS or Satellite</li>
    <li>Follow your Competitors online</li>
    <li>You could win $ 1,000</li>
  </ol>

  <div class="banner banner--url">RidgelineQuest2014.com</div>

  <section class="details">
    <div class="group">
      <div>Compete for</div>
      <div class="indent">Most Elevation Gain</div>
      <div class="indent">Most Miles</div>
      <div class="indent">Most Summits</div>
      <div class="indent">Best Photos</div>
      <div class="indent">Best Family Adventures</div>
    </div>
    <div class="group">
      <div>Prizes awarded by</div>
      <div class="indent">Age Class</div>
      <div class="indent">Gender</div>
      <div class="indent">Individuals</div>
      <div class="indent">Teams</div>
    </div>
    <div class="line">Where: Mountains of your Choice</div>
    <div class="line">Registration: $99 – Limited to 500 Participants</div>
    <div class="line">Optional: Rent a Trekbeam X4TM with Unlimited Tracking $99</div>
  </section>

  <footer class="sponsor">
    <span class="sponsor__mark"></span>
    <span class="sponsor__name">Institute for Glacier &amp; Frost Research</span>
    <span class="sponsor__note">Benefiting the Institute for Glacier &amp; Frost Research</span>
  </footer>
</main>
</body>
</html>
```